New Update: I am changing the title of the book and the back cover text. Title was too long before. Same style as before.
New Title: Under the Quiet Sky
New Subtitle: A Gardener’s Notes on Patience (italics on front cover)

Back cover text:
Under the Quiet Sky: A Gardener’s Notes on Patience offers clear, compassionate guidance for those recovering from total loss. Drawing from his experience as a Brennick Flood survivor, Tobias Quellhorst shares practical advice on insurance, rebuilding, and emotional healing, along with lessons in strength and community. This is not a book about tragedy; it’s about perseverance and renewal. Under the Quiet Sky is a trusted companion for anyone rebuilding life, home, and hope after disaster.

Font styles to use
Serif

Colors
EB3D1F
EC4F4E
F09395
F8D3D4
FCEDEE

Requirements
Should not have
• No pictures or anything related to fire on the cover.

```html
<!DOCTYPE html>
<html lang="en">
<head>
<meta charset="utf-8">
<title>Under the Quiet Sky — Book Cover</title>
<link rel="stylesheet" href="https://fonts.googleapis.com/css2?family=Playfair+Display:wght@700;900&family=Lora:wght@400;600;700&family=Libre+Baskerville:ital,wght@1,700&display=swap">
<style>
  :root {
    --backdrop: #d8d7d5;
    --red-bright: #eb3d1f;
    --red-coral: #ec4f4e;
    --pink-mid: #f09395;
    --pink-soft: #f8d3d4;
    --pink-pale: #fcedee;
    --red-deep: #5a100b;
    --red-core: #b02a18;
    --portrait-dark: #4a1a18;
    --portrait-light: #f09395;
  }
  * { box-sizing: border-box; margin: 0; padding: 0; }
  html, body { width: 1200px; height: 900px; overflow: hidden; background: var(--backdrop); }

  .cover-wrap {
    position: absolute; left: 110px; top: 100px;
    width: 980px; height: 700px;
    display: flex;
    box-shadow: 0 18px 40px rgba(0,0,0,0.25);
  }

  /* Back cover */
  .back-cover {
    position: relative; width: 460px; height: 100%;
    background: radial-gradient(ellipse at 55% 50%, var(--red-core) 0%, var(--red-deep) 85%);
    overflow: hidden;
  }
  .back-title {
    position: absolute; left: 20px; right: 20px; top: 52px;
    font-family: "Playfair Display", serif; font-weight: 900;
    font-size: 30px; line-height: 36px; color: var(--pink-soft);
    text-align: center; letter-spacing: 0.5px; text-transform: uppercase;
    white-space: nowrap;
  }
  .back-blurb {
    position: absolute; left: 44px; right: 44px; top: 112px;
    font-family: "Lora", serif; font-weight: 400;
    font-size: 15px; line-height: 27px; color: var(--pink-pale); text-align: center;
  }
  .back-blurb .accent { color: var(--pink-mid); }
  .author-band {
    position: absolute; left: 0; right: 0; top: 520px; height: 18px;
    background: var(--pink-pale);
  }
  .author-rule {
    position: absolute; left: 0; right: 0; top: 580px; height: 2px;
    background: var(--red-coral);
  }
  .author-portrait {
    position: absolute; left: 246px; top: 448px;
    width: 132px; height: 132px; border-radius: 50%;
    border: 3px solid var(--pink-mid);
    background: linear-gradient(160deg, var(--portrait-light) 0%, var(--portrait-dark) 75%);
  }
  .author-name {
    position: absolute; right: 34px; bottom: 36px;
    font-family: "Playfair Display", serif; font-weight: 900;
    font-size: 32px; color: var(--pink-soft); letter-spacing: 1px;
  }

  /* Spine */
  .spine {
    width: 56px; height: 100%;
    background: linear-gradient(90deg, var(--red-deep), var(--red-bright) 50%, var(--red-deep));
    display: flex; align-items: center; justify-content: center;
  }
  .spine-text {
    writing-mode: vertical-rl;
    font-family: "Lora", serif; font-weight: 700;
    font-size: 15px; letter-spacing: 1.5px; color: var(--pink-pale);
    text-transform: uppercase; white-space: nowrap;
  }
  .spine-text .accent { color: var(--pink-soft); }

  /* Front cover */
  .front-cover {
    position: relative; width: 464px; height: 100%;
    background: radial-gradient(ellipse at 60% 50%, var(--red-bright) 0%, var(--red-core) 45%, var(--red-deep) 100%);
    overflow: hidden;
  }
  .front-rule-top {
    position: absolute; left: 0; right: 0; top: 46px; height: 2px; background: var(--pink-mid);
  }
  .front-title {
    position: absolute; left: 40px; top: 88px;
    font-family: "Playfair Display", serif; font-weight: 900;
    font-size: 100px; line-height: 102px; color: var(--pink-pale);
    text-transform: uppercase; letter-spacing: -1px;
  }
  .front-title .title-line { display: block; }
  .front-title .title-accent { color: var(--pink-mid); display: flex; align-items: center; gap: 18px; }
  .title-accent::after {
    content: ""; display: block; width: 160px; height: 2px; background: var(--pink-mid);
  }
  .front-subtitle {
    position: absolute; right: 34px; bottom: 46px;
    font-family: "Libre Baskerville", serif; font-style: italic; font-weight: 700;
    font-size: 21px; color: var(--pink-pale);
  }
</style>
</head>
<body>
  <div class="cover-wrap">
    <section class="back-cover">
      <h2 class="back-title">Under the Quiet Sky</h2>
      <p class="back-blurb">
        <span class="accent">Under the Quiet Sky:</span> A Gardener’s Notes on Patience offers clear, compassionate guidance for those recovering from total loss. Drawing from his experience as a Brennick Flood survivor, <span class="accent">Tobias Quellhorst</span> shares practical advice on insurance, rebuilding, and emotional healing, along with lessons in strength and community. <span class="accent">This is not a book about tragedy; it’s about perseverance and renewal. Under the Quiet Sky is a trusted companion for anyone rebuilding life,</span> home, and hope after disaster.
      </p>
      <div class="author-band"></div>
      <div class="author-rule"></div>
      <div class="author-portrait" role="img" aria-label="Author portrait photograph"></div>
      <p class="author-name">Tobias Quellhorst</p>
    </section>
    <div class="spine">
      <p class="spine-text"><span class="accent">Under the Quiet Sky:</span> A Gardener’s Notes on Patience</p>
    </div>
    <section class="front-cover">
      <div class="front-rule-top"></div>
      <h1 class="front-title">
        <span class="title-line">Under</span>
        <span class="title-line title-accent">The</span>
        <span class="title-line">Quiet</span>
        <span class="title-line">Sky</span>
      </h1>
      <p class="front-subtitle">A Gardener’s Notes on Patience</p>
    </section>
  </div>
</body>
</html>
```